Kestrel Gardenworks Business Card

An eye catching, yet simple business card that includes;

1. our logo
2. office phone - 5083172946
3. email - kestrelgardenworks@mailbrook.com
4. website - www.kestrelgardenworks.com
5. instagram - @kestrelgardenworksnv

```html
<!DOCTYPE html>
<html lang="en">
<head>
<meta charset="utf-8">
<title>Kestrel Gardenworks Business Card</title>
<link href="https://fonts.googleapis.com/css2?family=Lora:wght@400;700&display=swap" rel="stylesheet">
<style>
  :root {
    --bg: #2b2b2d;
    --espresso: #1f0c04;
    --espresso-soft: #3a1c0c;
    --bronze: #a8692a;
    --bronze-light: #c58a45;
    --paper: #ffffff;
    --paper-shade: #ececec;
    --ink: #4a4a4a;
    --band: #1a1112;
  }
  * { margin: 0; padding: 0; box-sizing: border-box; }
  html, body { width: 1200px; height: 900px; overflow: hidden; }
  body {
    background: var(--bg);
    font-family: "Lora", Georgia, serif;
    position: relative;
  }
  .card {
    position: absolute;
    left: 280px;
    width: 640px;
    height: 366px;
    border-radius: 3px;
    overflow: hidden;
    box-shadow: 0 12px 30px rgba(0,0,0,.45);
  }
  .card--back { top: 62px; background: var(--espresso); }
  .pattern-field {
    position: absolute; inset: 0;
    background: linear-gradient(135deg, var(--espresso) 0%, var(--espresso-soft) 50%, var(--espresso) 100%);
  }
  .back-mark {
    position: absolute; right: 40px; bottom: 58px;
    color: var(--paper); font-weight: 700; font-size: 13px;
  }
  .card--front {
    top: 472px;
    background: linear-gradient(160deg, var(--paper) 40%, var(--paper-shade) 100%);
  }
  .front-shapes { position: absolute; inset: 0; }
  .brand {
    position: absolute; left: 56px; top: 150px;
    display: flex; align-items: center; gap: 12px;
    color: var(--espresso); font-weight: 700; font-size: 27px; line-height: 1.05;
  }
  .brand-dot { width: 34px; height: 34px; border-radius: 50%; background: var(--bronze); flex: none; }
  .contact-list {
    position: absolute; left: 336px; top: 112px;
    list-style: none; color: var(--ink); font-size: 15px;
  }
  .contact-list li { display: flex; align-items: center; gap: 10px; height: 26px; }
  .contact-list svg { width: 14px; height: 14px; flex: none; }
  .social-handle {
    position: absolute; left: 404px; top: 262px; height: 44px;
    display: flex; align-items: center; gap: 9px;
    color: var(--paper); font-size: 14px; white-space: nowrap;
  }
  .social-dot { width: 13px; height: 13px; border: 2px solid var(--paper); border-radius: 3px; flex: none; }
</style>
</head>
<body>

<section class="card card--back">
  <div class="pattern-field" role="img" aria-label="Repeating pattern of leaping animal silhouettes in bronze on dark brown"></div>
  <div class="back-mark">Kestrel Gardenworks</div>
</section>

<section class="card card--front">
  <svg class="front-shapes" viewBox="0 0 640 366" aria-hidden="true">
    <defs>
      <linearGradient id="bronzeTab" x1="0" y1="0" x2="1" y2="0">
        <stop offset="0" stop-color="#7a4716"/>
        <stop offset=".5" stop-color="#c58a45"/>
        <stop offset="1" stop-color="#8d5520"/>
      </linearGradient>
    </defs>
    <line x1="300" y1="58" x2="318" y2="250" stroke="#9a9a9a" stroke-width="1"/>
    <path d="M380 272 Q382 262 396 262 L640 262 L640 306 L406 306 L392 298 Z" fill="url(#bronzeTab)"/>
    <path d="M0 322 L376 322 L406 306 L406 366 L0 366 Z" fill="var(--band)"/>
  </svg>

  <div class="brand">
    <span class="brand-dot"></span>
    <span>Kestrel<br>Gardenworks</span>
  </div>

  <ul class="contact-list">
    <li>
      <svg viewBox="0 0 24 24"><path d="M6.6 10.8a15 15 0 0 0 6.6 6.6l2.2-2.2c.3-.3.7-.4 1-.2 1.1.4 2.3.6 3.6.6.6 0 1 .4 1 1V20c0 .6-.4 1-1 1A17 17 0 0 1 3 4c0-.6.4-1 1-1h3.5c.6 0 1 .4 1 1 0 1.3.2 2.5.6 3.6.1.3 0 .7-.2 1z" fill="var(--bronze)"/></svg>
      5083172946
    </li>
    <li>
      <svg viewBox="0 0 24 24"><rect x="2" y="5" width="20" height="14" rx="1" fill="var(--bronze)"/><path d="M2 6l10 7 10-7" stroke="#fff" stroke-width="1.6" fill="none"/></svg>
      kestrelgardenworks@mailbrook.com
    </li>
    <li>
      <svg viewBox="0 0 24 24" fill="none" stroke="var(--bronze)" stroke-width="1.8"><circle cx="12" cy="12" r="9"/><ellipse cx="12" cy="12" rx="4" ry="9"/><path d="M3 12h18M5 7h14M5 17h14"/></svg>
      www.kestrelgardenworks.com
    </li>
  </ul>

  <div class="social-handle">
    <span class="social-dot"></span>
    @kestrelgardenworksnv
  </div>
</section>

</body>
</html>
```